Lintel Systems

Looking for a web site design to market our services/applications
We write and supply bespoke web applications for the offshore and construction industries
Our initial product is Volk - rope access equipment management
Our buyers will be Rope Access companies via trade associations such as KEFOB and GLUMP
we have a logo designed see it attached we would like to see crisp professional designs based around these colours and design
we will supply web copy later
looking for home, services, blog, contact us, order and a general template (privacy, site map, T&C) pages
Updates
This payment will be for the homepage only
We can discuss other options (pages) with the successful designer
Regards
Norman
Industry/Entity Type
Construction
Look and feel

```html
<!DOCTYPE html>
<html lang="en">
<head>
<meta charset="utf-8">
<title>Lintel Systems — Home</title>
<link rel="stylesheet" href="https://fonts.googleapis.com/css2?family=Arimo:wght@400;700&display=swap">
<style>
:root{
  --blue:#0aa5e6;
  --blue-deep:#0d8fc6;
  --blue-light:#6fd0f5;
  --navy:#1d2a7a;
  --btn-dark:#0c7aa8;
  --text:#222;
  --white:#fff;
  --footer-bar:#0b8bc2;
}
*{box-sizing:border-box;margin:0;padding:0}
html,body{width:1200px;height:2603px;overflow:hidden;background:#fff}
body{font-family:"Arimo",Arial,sans-serif;color:var(--text);position:relative}
.abs{position:absolute}

/* hero */
.hero{left:0;top:0;width:1200px;height:674px;background:linear-gradient(100deg,#7aa6d2 0%,#5d8fc4 35%,#b9a482 58%,#c9ae86 80%,#a88d6a 100%)}
.header-box{left:101px;top:59px;width:998px;height:139px;background:var(--white);box-shadow:0 2px 6px rgba(0,0,0,.25);border-bottom:4px solid var(--blue)}
.brand{left:22px;top:30px;display:flex;align-items:center;gap:14px}
.brand-mark{width:62px;height:62px;background:var(--blue);border-radius:8px}
.brand-name{font-size:34px;line-height:36px;color:var(--navy)}
.social{right:228px;top:10px;display:flex;gap:10px}
.social span{width:26px;height:26px;background:var(--blue-deep);border-radius:4px}
.search{right:22px;top:6px;width:212px;height:34px;background:var(--blue);color:#fff;font-size:13px;padding:9px 12px}
.search svg{position:absolute;right:10px;top:8px}
.nav{left:400px;top:72px;display:flex}
.nav a{font-size:22px;color:#111;text-decoration:none;padding:8px 24px;border-left:1px solid #ddd}
.nav a:first-child{border-left:none;color:var(--blue)}
.caption{left:347px;top:400px;width:504px;height:93px;background:rgba(13,143,198,.88);color:#fff;font-size:29px;text-align:center;line-height:36px;padding-top:10px}
.order-now{left:478px;top:495px;width:244px;height:59px;background:var(--blue);color:#fff;font-size:30px;display:flex;align-items:center;justify-content:center;gap:10px}
.dots{left:530px;top:624px;display:flex;gap:10px}
.dots span{width:18px;height:18px;border-radius:50%;background:#fff}
.dots span:first-child{background:var(--blue)}

/* section titles */
.section-title{left:0;width:1200px;display:flex;align-items:center;justify-content:center;gap:14px;font-size:31px;color:var(--white)}
.section-title i{display:block;width:250px;height:2px;background:currentColor;position:relative}
.section-title i::after{content:"";position:absolute;top:-6px;width:14px;height:14px;border-radius:50%;background:currentColor}
.section-title i.l::after{right:-2px}
.section-title i.r::after{left:-2px}

/* services */
.services{left:0;top:674px;width:1200px;height:408px;background:linear-gradient(#6fd0f5,#1bb1ec 40%,#0aa5e6)}
.service{width:240px;text-align:center;color:#fff}
.service .photo{width:114px;height:114px;border-radius:50%;margin:0 auto;border:4px solid #0c7aa8;background:linear-gradient(135deg,#9bb6c8,#3d5b73)}
.service p{font-size:16px;line-height:25px;margin-top:20px}
.btn{background:var(--btn-dark);color:#fff;font-size:16px;display:inline-flex;align-items:center;gap:8px;padding:0 12px;height:32px}

/* about */
.about{left:0;top:1082px;width:1200px;height:419px;background:linear-gradient(#fff 40%,#e8e8e8)}
.about-title{left:124px;top:50px;font-size:31px;color:var(--blue);display:flex;align-items:center;gap:10px}
.about-title i{display:block;width:360px;height:2px;background:var(--blue);position:relative}
.about-title i::before{content:"";position:absolute;left:-2px;top:-6px;width:14px;height:14px;border-radius:50%;background:var(--blue)}
.about-text{left:157px;top:112px;width:508px;font-size:16px;line-height:26px;color:#111}
.read-more{left:537px;top:319px;height:35px;background:var(--blue)}
.order-box{left:731px;top:46px;width:329px;height:330px;background:linear-gradient(#7fd6f6,#bfe9f9 60%,#eef8fc);box-shadow:0 3px 10px rgba(0,0,0,.2);padding:14px 20px}
.order-box h3{font-size:27px;font-weight:400;text-align:center;color:#111}
.order-box .sub{font-size:15px;color:#fff;text-align:center;line-height:22px;margin-top:6px}
.field{display:flex;justify-content:space-between;align-items:center;margin-top:20px;font-size:16px}
.field span{width:162px;height:22px;background:#fff;border:1px solid #9cc}
.order-submit{position:absolute;right:22px;bottom:44px;height:35px;background:var(--blue);font-size:17px}

/* testimonial */
.testimonial{left:0;top:1501px;width:1200px;height:332px;background:linear-gradient(#0aa5e6,#39b8ee 55%,#c4eafb)}
.testimonial h2{position:absolute;top:40px;width:100%;text-align:center;font-size:30px;font-weight:400;color:#fff}
.testimonial p{position:absolute;left:205px;top:122px;width:750px;text-align:center;font-size:17px;font-weight:700;line-height:25px;color:#fff}
.quote{font-size:90px;color:#fff;opacity:.85;font-family:Georgia,serif}

/* blog */
.blog{left:0;top:1833px;width:1200px;height:497px;background:#fff}
.blog .section-title{color:var(--blue);top:54px}
.avatar{width:130px;height:130px;border-radius:50%;border:4px solid #bfe9f9;background:linear-gradient(#d9dee2,#8b98a3)}
.post h4{font-size:18px;font-weight:400;color:var(--blue)}
.post .date{font-size:13px;color:var(--blue);margin-top:3px}
.post p{font-size:13px;line-height:25px;color:#333;margin-top:8px}

/* footer */
.footer{left:0;top:2330px;width:1200px;height:223px;background:var(--blue);color:#fff}
.footer .brand{left:122px;top:57px}
.footer .brand-mark{width:90px;height:90px;background:#0d8fc6;border:3px solid #fff}
.footer .brand-name{font-size:34px;color:#1d2a7a}
.contact{left:448px;top:50px;font-size:17px;line-height:48px}
.contact div{display:flex;align-items:center;gap:14px}
.fdiv{top:40px;width:2px;height:150px;background:rgba(0,0,0,.12)}
.flinks{left:746px;top:53px;font-size:17px;font-weight:700;line-height:25px}
.follow{left:925px;top:53px}
.follow h5{font-size:18px}
.follow .row{display:flex;gap:12px;margin-top:14px}
.follow .row span{width:28px;height:28px;border-radius:4px;background:#fff;opacity:.9}
.bottom-bar{left:0;top:2553px;width:1200px;height:50px;background:var(--footer-bar);color:#fff;font-size:11px}
</style>
</head>
<body>

<section class="hero abs" role="img" aria-label="Photograph of a climber on a rope abseiling down a sunlit rock face against a blue sky">
  <div class="header-box abs">
    <div class="brand abs"><div class="brand-mark"></div><div class="brand-name">Lintel Systems</div></div>
    <div class="social abs"><span></span><span></span><span></span></div>
    <div class="search abs">Search..
      <svg width="18" height="18" viewBox="0 0 18 18"><circle cx="7" cy="7" r="5" fill="none" stroke="#fff" stroke-width="2.5"/><line x1="11" y1="11" x2="16" y2="16" stroke="#fff" stroke-width="2.5"/></svg>
    </div>
    <nav class="nav abs"><a>Home</a><a>Services</a><a>Blog</a><a>Contact Us</a><a>Order</a></nav>
  </div>
  <div class="caption abs">Want to purchase&nbsp; Volk - rope<br>access equipment</div>
  <div class="order-now abs">Order Now
    <svg width="28" height="28" viewBox="0 0 28 28"><circle cx="14" cy="14" r="12" fill="none" stroke="#fff" stroke-width="2"/><path d="M9 9l5 5-5 5M14 9l5 5-5 5" fill="none" stroke="#fff" stroke-width="2"/></svg>
  </div>
  <div class="dots abs"><span></span><span></span><span></span><span></span><span></span></div>
</section>

<section class="services abs">
  <div class="section-title abs" style="top:40px"><i class="l"></i>OUR SERVICES<i class="r"></i></div>
  <div class="service abs" style="left:124px;top:103px">
    <div class="photo" role="img" aria-label="Photo of hands working on equipment"></div>
    <p>dummy text of the printing<br>and typesetting industry.<br>Lorem Ipsum has been<br>the industry's standard</p>
    <div class="btn" style="margin-top:24px">Learn More <svg width="18" height="18" viewBox="0 0 28 28"><circle cx="14" cy="14" r="12" fill="none" stroke="#fff" stroke-width="2.5"/><path d="M9 9l5 5-5 5M14 9l5 5-5 5" fill="none" stroke="#fff" stroke-width="2.5"/></svg></div>
  </div>
  <div class="service abs" style="left:364px;top:103px">
    <div class="photo" role="img" aria-label="Photo of a finger touching a digital interface"></div>
    <p>dummy text of the printing<br>and typesetting industry.<br>Lorem Ipsum has been<br>the industry's standard</p>
    <div class="btn" style="margin-top:24px">Learn More <svg width="18" height="18" viewBox="0 0 28 28"><circle cx="14" cy="14" r="12" fill="none" stroke="#fff" stroke-width="2.5"/><path d="M9 9l5 5-5 5M14 9l5 5-5 5" fill="none" stroke="#fff" stroke-width="2.5"/></svg></div>
  </div>
  <div class="service abs" style="left:593px;top:103px">
    <div class="photo" role="img" aria-label="Photo of a person typing on a laptop"></div>
    <p>dummy text of the printing<br>and typesetting industry.<br>Lorem Ipsum has been<br>the industry's standard</p>
    <div class="btn" style="margin-top:24px">Learn More <svg width="18" height="18" viewBox="0 0 28 28"><circle cx="14" cy="14" r="12" fill="none" stroke="#fff" stroke-width="2.5"/><path d="M9 9l5 5-5 5M14 9l5 5-5 5" fill="none" stroke="#fff" stroke-width="2.5"/></svg></div>
  </div>
  <div class="service abs" style="left:833px;top:103px">
    <div class="photo" role="img" aria-label="Photo of rope access carabiners and gear"></div>
    <p>dummy text of the printing<br>and typesetting industry.<br>Lorem Ipsum has been<br>the industry's standard</p>
    <div class="btn" style="margin-top:24px">Learn More <svg width="18" height="18" viewBox="0 0 28 28"><circle cx="14" cy="14" r="12" fill="none" stroke="#fff" stroke-width="2.5"/><path d="M9 9l5 5-5 5M14 9l5 5-5 5" fill="none" stroke="#fff" stroke-width="2.5"/></svg></div>
  </div>
</section>

<section class="about abs">
  <div class="about-title abs">ABOUT US<i></i></div>
  <p class="about-text abs">Lorem Ipsum is simply dummy text of the printing and typesetting industry. Lorem Ipsum has been the industry's standard dummy text ever since the 1500s, when an unknown printer took a galley of type and scrambled it to make a type specimen book. It has survived not only five centuries, but also the leap into electronic typesetting, remaining essentially unchanged. It was popularised in the 1960s with the release of Letraset sheets containing Lorem Ipsum passages.</p>
  <div class="btn read-more abs">Read More <svg width="20" height="20" viewBox="0 0 28 28"><circle cx="14" cy="14" r="12" fill="none" stroke="#fff" stroke-width="2.5"/><path d="M9 9l5 5-5 5M14 9l5 5-5 5" fill="none" stroke="#fff" stroke-width="2.5"/></svg></div>
  <form class="order-box abs">
    <h3>Order your products?</h3>
    <div class="sub">Now you can easily order ur<br>products here!</div>
    <div class="field">User Name<span></span></div>
    <div class="field">Email Id<span></span></div>
    <div class="field">Product Name<span style="position:relative"><svg style="position:absolute;right:4px;top:7px" width="8" height="6" viewBox="0 0 8 6"><path d="M0 0h8L4 6z" fill="#222"/></svg></span></div>
    <div class="btn order-submit">Order Now</div>
  </form>
</section>

<section class="testimonial abs" role="img" aria-label="Faint background photo of a group of business people">
  <h2>What our client's say</h2>
  <div class="quote abs" style="left:150px;top:40px">“</div>
  <p>Lorem Ipsum is simply dummy text of the printing and typesetting industry. Lorem Ipsum has been the industry's standard dummy text ever since the 1500s, when an unknown printer took a galley of type and scrambled it to make a type specimen book. It has survived not only five centuries, but also the leap into electronic typesetting, remaLorem Ipsum is simply dummy text of the printingcontaining Lorem Ipsum passages.</p>
  <div class="quote abs" style="left:970px;top:200px">”</div>
</section>

<section class="blog abs">
  <div class="section-title abs"><i class="l"></i>RECENT BLOG<i class="r"></i></div>
  <div class="avatar abs" style="left:147px;top:137px" role="img" aria-label="Portrait photo of a blog author"></div>
  <article class="post abs" style="left:319px;top:138px;width:680px">
    <h4>Lorem Ipsum is simply text</h4>
    <div class="date">October 6th,2014</div>
    <p>Lorem Ipsum is simply dummy text of the printing and typesetting industry. Lorem Ipsum has been the industry's standard dummy text ever since the 1500s, when an unknown printer took a galley of type and scrambled it to make a type specimen book. dummy text of the printingcontaining Lorem Ipsum passages.</p>
  </article>
  <article class="post abs" style="left:170px;top:316px;width:680px">
    <h4>Lorem Ipsum is simply text</h4>
    <div class="date">October 7th,2014</div>
    <p>Lorem Ipsum is simply dummy text of the printing and typesetting industry. Lorem Ipsum has been the industry's standard dummy text ever since the 1500s, when an unknown printer took a galley of type and scrambled it to make a type specimen book. dummy text of the printingcontaining Lorem Ipsum passages.</p>
  </article>
  <div class="avatar abs" style="left:877px;top:308px" role="img" aria-label="Portrait photo of a blog author"></div>
</section>

<footer class="footer abs">
  <div class="brand abs"><div class="brand-mark"></div><div class="brand-name">Lintel<br>Systems</div></div>
  <div class="contact abs">
    <div><svg width="26" height="26" viewBox="0 0 26 26"><rect x="1" y="1" width="24" height="24" fill="none" stroke="#fff" stroke-width="2"/><path d="M13 6v14M6 13h14" stroke="#fff" stroke-width="2"/></svg>About us</div>
    <div><svg width="26" height="26" viewBox="0 0 24 24"><path d="M6.6 10.8a15 15 0 006.6 6.6l2.2-2.2c.3-.3.7-.4 1-.2 1.1.4 2.3.6 3.6.6.6 0 1 .4 1 1V20c0 .6-.4 1-1 1A17 17 0 013 4c0-.6.4-1 1-1h3.5c.6 0 1 .4 1 1 0 1.3.2 2.5.6 3.6.1.3 0 .7-.2 1z" fill="#fff"/></svg>(123) 456-7890</div>
    <div><svg width="26" height="20" viewBox="0 0 26 20"><rect x="1" y="1" width="24" height="18" fill="none" stroke="#fff" stroke-width="2"/><path d="M1 1l12 10L25 1" fill="none" stroke="#fff" stroke-width="2"/></svg>lintelsystems@info.com</div>
  </div>
  <div class="fdiv abs" style="left:710px"></div>
  <div class="flinks abs">Home<br>Services<br>Blog<br>Contact Us<br>Order</div>
  <div class="fdiv abs" style="left:880px"></div>
  <div class="follow abs">
    <h5>Fallow Us</h5>
    <div class="row"><span></span><span></span><span></span><span></span></div>
    <div class="row"><span></span><span></span><span></span><span></span></div>
  </div>
</footer>
<div class="bottom-bar abs">
  <div class="abs" style="left:550px;top:19px">All Rights Reserved</div>
  <div class="abs" style="left:945px;top:19px">Site Map &nbsp;·&nbsp; Privacy &nbsp;·&nbsp; Site Credits</div>
</div>

</body>
</html>
```